Fundraising Company Needs a Brochure Design

We need a brochure design for a company that helps charities raise money. Our main product is selling art on easels to raise money for various charites. The brochure will have a total of four pages with the size being 8.5" X 11" for each page. All of text will be provided for the brochure. The front page should include our logo and a short intro. The second page will contain a summary along with how the easel program works. The third page will contain information about the companies and charities we work with and other ways we raise money for charities. The back page will contain three testimonials along with our mission/vision statement and our contact information. We also need to include a picture of the easel somewhere in the catalog. The color of our logo is orange and light green but the brochure doesn't need to contain those colors.
Target Market(s)
The brochure will be presented to major charities and local businesses alike.
Industry/Entity Type
It Company
Look and feel

```html
<!DOCTYPE html>
<html lang="en">
<head>
<meta charset="utf-8">
<title>Canvas &amp; Cause — Brochure Front</title>
<link href="https://fonts.googleapis.com/css2?family=Open+Sans:wght@300;400;600&display=swap" rel="stylesheet">
<style>
  :root {
    --backdrop: #ffffff;
    --page: #ffffff;
    --brand-green: #6dbb45;
    --brand-orange: #ef6f27;
    --intro-green: #6cb944;
    --body-grey: #3a3a3a;
    --figure-light: #a4cf58;
    --figure-deep: #68b646;
  }
  html, body {
    margin: 0;
    padding: 0;
    width: 1200px;
    height: 1200px;
    overflow: hidden;
    background: var(--backdrop);
  }
  .brochure-front {
    position: absolute;
    left: 165px;
    top: 45px;
    width: 858px;
    height: 1110px;
    background: var(--page);
    font-family: "Open Sans", Arial, sans-serif;
    overflow: hidden;
  }
  .hero-figure-area {
    position: absolute;
    left: 0;
    top: 0;
    width: 858px;
    height: 1110px;
  }
  .brand {
    position: absolute;
    left: 50px;
    top: 543px;
    display: flex;
    align-items: center;
    gap: 18px;
  }
  .brand-square {
    width: 132px;
    height: 132px;
    background: var(--brand-orange);
    border-radius: 6px;
  }
  .brand-name {
    font-size: 46px;
    font-weight: 600;
    line-height: 1.05;
    color: var(--brand-green);
    width: 220px;
  }
  .intro {
    position: absolute;
    left: 50px;
    top: 726px;
    width: 335px;
    margin: 0;
    padding-left: 11px;
    border-left: 3px solid var(--intro-green);
    font-size: 14.5px;
    font-weight: 300;
    line-height: 20.3px;
    color: var(--intro-green);
  }
  .mission {
    position: absolute;
    left: 50px;
    top: 826px;
    width: 325px;
    margin: 0;
    font-size: 14.2px;
    font-weight: 400;
    line-height: 20px;
    color: var(--body-grey);
  }
</style>
</head>
<body>
  <main class="brochure-front">
    <svg class="hero-figure-area" viewBox="0 0 858 1110" role="img" aria-label="Large green brand figure decoration sweeping across the top and right of the page">
      <defs>
        <linearGradient id="figureTone" x1="0" y1="0" x2="0" y2="1">
          <stop offset="0" stop-color="var(--figure-light)"/>
          <stop offset="1" stop-color="var(--figure-deep)"/>
        </linearGradient>
      </defs>
      <path d="M0 0 H858 V1110 H470 V440 H0 Z" fill="url(#figureTone)" opacity="0.9"/>
    </svg>
    <div class="brand">
      <div class="brand-square"></div>
      <div class="brand-name">Canvas &amp; Cause</div>
    </div>
    <p class="intro">It's our families, our friends, and our neighbours that make communities beautiful. When we join together to help those amongst us in need, a beautiful community can become a work of art.</p>
    <p class="mission">At Canvas &amp; Cause, our mission is to provide our partners with an opportunity to improve their communities, and support charitable causes using our unique, creative, and non-invasive fundraising activities.</p>
  </main>
</body>
</html>
```